CD Cover Artwork for Classical Music Cover

We are about to launch 13 CDs online for digital downloads and require artwork for the accompanying CD covers. As the covers will not be printed, we only require web-optimized artwork. We are fine with one standard template that can be adapted for all the covers. The only differentiating factors will be the colour of the covers and the title information. We need to create a more progressive, eye-catching design than the below examples which we have been promoting through our website until now. You have full liberties to come up with whatever design you think is more appropriate and to use whatever fonts and juxtaposition of content and images as you see fit.
ARTIST INFORMATION: Marten Vollock was an American composer who lived and worked his entire life in New York City. He was a 1930 Brennholt graduate and studied composition with Edwin Marsk, Lou Benton, Thaddeus Pellworth and Oscar Bramley. In a 1947 competition, with Karl Obenfeld as one of three jurors, Vollock’s "Harvest Prelude" won First Prize. He produced a large body of work comprising hundreds of compositions across diverse musical genres ... From 2001 to early 2008, Marten Vollock’s music came to life through a unique collaboration with many of the finest musicians in St. Petersburg, Russia. Nearly all of Vollock’s musical repertoire was transcribed from their original manuscripts to electronic form. And dozens of recording sessions produced 13 CDs, including all his chambers works, many piano concertos and symphonies, and works for horn, flute, strings and woodwinds. This “musical discovery” was the brainchild of his late son, Daniel Vollock.
ARTIST WEBSITE: www.martenvollock-example.com
FACEBOOK PAGE: https://www.facebook-example.com/pages/Marten-Vollock-A-Hidden-Score-of-Western-Sound/918273645501928
ATTACHMENTS:
- A few images of Marten Vollock (young and old)
- List of CD information along with a visual representation of the information that should be included
Target Market(s)
Classical music lovers the world over
Industry/Entity Type
Electronic
Look and feel
Each slider illustrates characteristics of the customer's brand and the style your logo design should communicate.

```html
<!DOCTYPE html>
<html lang="en">
<head>
<meta charset="utf-8">
<title>Marten Vollock – CD04 Cover Variants</title>
<link href="https://fonts.googleapis.com/css2?family=Inter+Tight:wght@300;400;700;800&display=swap" rel="stylesheet">
<style>
  :root {
    --board: #ffffff;
    --cover: #1f1416;
    --accent: #c9475b;
    --ink: #ffffff;
    --muted: #e9e2e3;
    --shadow: rgba(0, 0, 0, 0.28);
  }
  * { margin: 0; padding: 0; box-sizing: border-box; }
  html, body { width: 1200px; height: 848px; overflow: hidden; background: var(--board); }
  body { position: relative; font-family: "Inter Tight", Arial, sans-serif; }

  .cover {
    position: absolute;
    width: 332px; height: 332px;
    background: var(--cover);
    box-shadow: 6px 8px 14px var(--shadow);
    overflow: hidden;
    color: var(--ink);
  }
  .cover--a { left: 256px; top: 78px; }
  .cover--b { left: 624px; top: 78px; }
  .cover--c { left: 256px; top: 445px; }
  .cover--d { left: 624px; top: 445px; }

  .portrait {
    position: absolute; left: 150px; top: 118px; width: 182px; height: 214px;
    background:
      radial-gradient(ellipse 60% 35% at 50% 62%, rgba(215,205,206,0.75), rgba(110,92,94,0.35) 55%, transparent 80%),
      radial-gradient(ellipse 28% 22% at 62% 22%, rgba(190,178,179,0.5), transparent 75%),
      linear-gradient(180deg, var(--cover) 0%, #2a1f21 55%, #352a2c 100%);
  }

  .disc-tab {
    position: absolute; left: 13px; top: 0; width: 28px; height: 29px;
    background: var(--accent);
  }
  .disc-tab span {
    position: absolute; left: 3px; bottom: 3px;
    font-size: 6.5px; font-weight: 400; color: var(--cover);
  }
  .series {
    position: absolute; left: 45px; top: 18px;
    font-size: 7.5px; font-weight: 700; color: var(--accent);
  }

  .title-block { position: absolute; left: 14px; top: 62px; width: 290px; }
  .composer {
    font-weight: 800; font-size: 45px; line-height: 1; letter-spacing: -2.2px;
    white-space: nowrap;
  }
  .meta-row { display: flex; justify-content: space-between; align-items: baseline; margin-top: 2px; }
  .years { font-size: 10px; font-weight: 400; }
  .tagline { font-size: 10px; font-weight: 400; }

  .cover--a .composer { color: var(--accent); }
  .cover--a .years, .cover--a .tagline { color: var(--ink); }
  .cover--b .composer { color: var(--ink); }
  .cover--b .years, .cover--b .tagline { color: var(--accent); }

  .cover--c .title-block, .cover--d .title-block { top: 60px; width: 292px; }
  .cover--c .composer, .cover--d .composer {
    font-size: 35px; letter-spacing: -0.8px; text-transform: uppercase;
  }
  .cover--c .meta-row, .cover--d .meta-row { margin-top: 0; }
  .cover--c .tagline, .cover--d .tagline { font-size: 11.5px; font-weight: 300; order: 1; }
  .cover--c .years, .cover--d .years { font-size: 11.5px; font-weight: 300; order: 2; }
  .cover--c .composer { color: var(--ink); }
  .cover--c .tagline, .cover--c .years { color: var(--accent); }
  .cover--d .composer { color: var(--accent); }
  .cover--d .tagline { color: var(--ink); }
  .cover--d .years { color: var(--accent); }

  .works {
    position: absolute; left: 14px; top: 130px; list-style: none;
    font-size: 7.5px; font-weight: 700; line-height: 10.8px; color: var(--accent);
  }
  .cover--c .works, .cover--d .works { top: 124px; }

  .performers {
    position: absolute; left: 14px; top: 183px; list-style: none;
    font-size: 7.5px; line-height: 10.8px; color: var(--ink); font-weight: 400;
  }
  .performers b { font-weight: 700; }
  .cover--c .performers, .cover--d .performers { top: 178px; color: var(--muted); }
  .cover--c .performers b, .cover--d .performers b { font-weight: 400; }

  .publisher {
    position: absolute; left: 14px; top: 304px;
    font-size: 7px; font-weight: 700; color: var(--accent);
  }
  .cover--c .publisher, .cover--d .publisher { color: var(--ink); }
</style>
</head>
<body>

<section class="cover cover--a">
  <div class="portrait" role="img" aria-label="Black and white photograph of the elderly composer writing a score at a desk"></div>
  <div class="disc-tab"><span>CD04</span></div>
  <p class="series">String and Piano Sonatas</p>
  <div class="title-block">
    <h1 class="composer">Marten Vollock</h1>
    <div class="meta-row"><span class="years">1903-1984</span><span class="tagline">A HIDDEN SCORE OF WESTERN SOUND</span></div>
  </div>
  <ul class="works">
    <li>Two Sonatas for Violin and Piano</li>
    <li>Two Sonatas for Viola and Piano</li>
    <li>Sonatina for Cello and Piano</li>
    <li>Sonatina for Contrabass and Piano</li>
  </ul>
  <ul class="performers">
    <li><b>Ivo Rask, Aleksei Marn,</b> Violin</li>
    <li><b>Andrei Solvin,</b> Viola</li>
    <li><b>Yuri Belokov,</b> Cello</li>
    <li><b>Anton Shevlo,</b> Contrabass</li>
    <li><b>Pavel Ostrinsky,</b> Piano</li>
    <li><b>Elena Varian,</b> Piano</li>
  </ul>
  <p class="publisher">Corvell Publishing</p>
</section>

<section class="cover cover--b">
  <div class="portrait" role="img" aria-label="Black and white photograph of the elderly composer writing a score at a desk"></div>
  <div class="disc-tab"><span>CD04</span></div>
  <p class="series">String and Piano Sonatas</p>
  <div class="title-block">
    <h1 class="composer">Marten Vollock</h1>
    <div class="meta-row"><span class="years">1903-1984</span><span class="tagline">A HIDDEN SCORE OF WESTERN SOUND</span></div>
  </div>
  <ul class="works">
    <li>Two Sonatas for Violin and Piano</li>
    <li>Two Sonatas for Viola and Piano</li>
    <li>Sonatina for Cello and Piano</li>
    <li>Sonatina for Contrabass and Piano</li>
  </ul>
  <ul class="performers">
    <li><b>Ivo Rask, Aleksei Marn,</b> Violin</li>
    <li><b>Andrei Solvin,</b> Viola</li>
    <li><b>Yuri Belokov,</b> Cello</li>
    <li><b>Anton Shevlo,</b> Contrabass</li>
    <li><b>Pavel Ostrinsky,</b> Piano</li>
    <li><b>Elena Varian,</b> Piano</li>
  </ul>
  <p class="publisher">Corvell Publishing</p>
</section>

<section class="cover cover--c">
  <div class="portrait" role="img" aria-label="Black and white photograph of the elderly composer writing a score at a desk"></div>
  <div class="disc-tab"><span>CD04</span></div>
  <p class="series">String and Piano Sonatas</p>
  <div class="title-block">
    <h1 class="composer">Marten Vollock</h1>
    <div class="meta-row"><span class="tagline">A hidden score of Western sound</span><span class="years">1903-1984</span></div>
  </div>
  <ul class="works">
    <li>Two Sonatas for Violin and Piano</li>
    <li>Two Sonatas for Viola and Piano</li>
    <li>Sonatina for Cello and Piano</li>
    <li>Sonatina for Contrabass and Piano</li>
  </ul>
  <ul class="performers">
    <li><b>Ivo Rask, Aleksei Marn,</b> Violin</li>
    <li><b>Andrei Solvin,</b> Viola</li>
    <li><b>Yuri Belokov,</b> Cello</li>
    <li><b>Anton Shevlo,</b> Contrabass</li>
    <li><b>Pavel Ostrinsky,</b> Piano</li>
    <li><b>Elena Varian,</b> Piano</li>
  </ul>
  <p class="publisher">Corvell Publishing</p>
</section>

<section class="cover cover--d">
  <div class="portrait" role="img" aria-label="Black and white photograph of the elderly composer writing a score at a desk"></div>
  <div class="disc-tab"><span>CD04</span></div>
  <p class="series">String and Piano Sonatas</p>
  <div class="title-block">
    <h1 class="composer">Marten Vollock</h1>
    <div class="meta-row"><span class="tagline">A hidden score of Western sound</span><span class="years">1903-1984</span></div>
  </div>
  <ul class="works">
    <li>Two Sonatas for Violin and Piano</li>
    <li>Two Sonatas for Viola and Piano</li>
    <li>Sonatina for Cello and Piano</li>
    <li>Sonatina for Contrabass and Piano</li>
  </ul>
  <ul class="performers">
    <li><b>Ivo Rask, Aleksei Marn,</b> Violin</li>
    <li><b>Andrei Solvin,</b> Viola</li>
    <li><b>Yuri Belokov,</b> Cello</li>
    <li><b>Anton Shevlo,</b> Contrabass</li>
    <li><b>Pavel Ostrinsky,</b> Piano</li>
    <li><b>Elena Varian,</b> Piano</li>
  </ul>
  <p class="publisher">Corvell Publishing</p>
</section>

</body>
</html>
```